Ridgeway Builders, Inc. Concrete cutting special flyer , 10% off for new customers

Flyer to send to potential customers and business associates and general contractors - specializing in Concrete-Flatwork
Concrete Repair
Concrete Sidewalks
Patios & Driveways
Stoops, Porches And Staircase
Foundation Contractors--Concrete
Facade Restoration
Concrete
Patios
Driveways
Walkways
Commercial Concrete Work
Concrete Restoration
Building Alterations
Foundations - Concrete
Concrete Repairs
rbwxpo.com

Target Market(s)

Homeowners, business owners & general contractors

Industry/Entity Type

Construction

Font styles to use
Serif

Colors
FFC000
F8CF3A
FAE287
FDF2CF
FEFAEE
EB3D1F
EC4F4E
F09395
F8D3D4
FCEDEE

Requirements
Must have
• General Contracting, masonry - Must have Logo Please see list of services Ridgeway Builders NY, Inc., has to offer. Concrete-Flatwork Concrete Repair Concrete Sidewalks Patios & Driveways Stoops, Porches And Staircase Foundation Contractors--Concrete Facade Restoration Concrete Patios Driveways Walkways Commercial Concrete Work Concrete Restoration Building Alterations Foundations - Concrete Concrete Repairs
Nice to have
• List of services - Logo - Black & Gold with a bold color to stand out (preferably reds)

```html
<!DOCTYPE html>
<html lang="en">
<head>
<meta charset="utf-8">
<title>Ridgeway Builders – Excavation Flyer</title>
<link href="https://fonts.googleapis.com/css2?family=Oswald:wght@600;700&family=Poppins:wght@400;500;600;700&display=swap" rel="stylesheet">
<style>
  :root {
    --page-bg: #e2e2e2;
    --paper: #ffffff;
    --forest: #1b4328;
    --forest-deep: #1c4a2b;
    --mint: #3fae5c;
    --charcoal: #333333;
    --slate: #555555;
    --mist: #efefef;
    --ink: #1a1a1a;
    --alert-red: #e8211d;
  }
  * { box-sizing: border-box; margin: 0; padding: 0; }
  html, body { width: 1200px; height: 2496px; overflow: hidden; }
  body { background: var(--page-bg); font-family: "Poppins", sans-serif; position: relative; }

  .flyer {
    position: absolute; left: 50px; top: 470px;
    width: 1100px; height: 1555px;
    background: var(--paper); overflow: hidden;
  }
  .abs { position: absolute; }

  /* header */
  .brand { left: 66px; top: 90px; display: flex; align-items: center; gap: 14px; }
  .brand-mark { width: 26px; height: 26px; background: var(--forest); flex-shrink: 0; }
  .brand-name { font-weight: 700; color: var(--forest); font-size: 30px; line-height: 1.15; }

  .headline {
    left: 62px; top: 252px;
    font-family: "Oswald", sans-serif; font-weight: 700;
    font-size: 118px; line-height: 1; color: var(--forest);
    letter-spacing: -2px; transform: scaleX(.78); transform-origin: left top;
    white-space: nowrap;
  }
  .subhead {
    left: 66px; top: 371px;
    font-weight: 700; font-size: 29px; color: var(--slate); letter-spacing: .3px;
    white-space: nowrap;
  }

  .hero-art { left: 0; top: 0; }

  /* specialties band */
  .band-dark { left: 0; top: 433px; width: 1100px; height: 410px; background: var(--charcoal); }
  .tagline {
    left: 66px; top: 472px; padding-left: 16px;
    border-left: 4px solid var(--mint);
    color: #fff; font-weight: 600; font-size: 19px; line-height: 1.2;
    white-space: nowrap;
  }
  .specialize {
    left: 66px; top: 582px; color: #fff; font-size: 33px; font-weight: 400;
    white-space: nowrap;
  }
  .specialize b { font-weight: 700; }
  .specialize .hot { color: var(--alert-red); font-weight: 700; }

  .service-col { top: 652px; list-style: none; }
  .service-col li {
    position: relative; padding-left: 22px;
    color: #fff; font-weight: 600; font-size: 17px; line-height: 1.15;
    margin-bottom: 14px; white-space: nowrap;
  }
  .service-col li::before {
    content: "›"; position: absolute; left: 0; top: -4px;
    color: var(--mint); font-size: 24px; font-weight: 700;
  }

  /* lower section */
  .band-light { left: 0; top: 843px; width: 1100px; height: 565px; background: var(--mist); }
  .machine-photo {
    left: 0; top: 843px; width: 660px; height: 577px;
    background: linear-gradient(140deg, #e8e8e8 0%, #d9d9d9 30%, #e4a93a 55%, #d18d22 70%, #8c8c8c 90%);
    clip-path: polygon(0 0, 100% 0, 76% 10%, 80% 58%, 100% 92%, 82% 98%, 0 100%);
  }

  .badge { left: 71px; top: 804px; width: 260px; height: 260px; }
  .badge .burst {
    position: absolute; left: 38px; top: 38px; width: 184px; height: 184px;
    background: var(--mint);
  }
  .badge .burst:nth-child(2) { transform: rotate(15deg); }
  .badge .burst:nth-child(3) { transform: rotate(30deg); }
  .badge .burst:nth-child(4) { transform: rotate(45deg); }
  .badge .burst:nth-child(5) { transform: rotate(60deg); }
  .badge .burst:nth-child(6) { transform: rotate(75deg); }
  .badge-copy {
    position: absolute; inset: 0; transform: rotate(-6deg);
    display: flex; flex-direction: column; align-items: center; justify-content: center;
    color: #fff; font-family: "Oswald", sans-serif; text-align: center;
  }
  .badge-copy .deal { display: flex; align-items: flex-end; line-height: 1; white-space: nowrap; }
  .badge-copy .pct { font-size: 86px; font-weight: 700; letter-spacing: -2px; line-height: .95; }
  .badge-copy .off { font-size: 38px; font-weight: 700; margin-left: 4px; margin-bottom: 6px; }
  .badge-copy .for { font-family: "Poppins", sans-serif; font-size: 16px; line-height: 1.2; margin-top: 2px; }
  .badge-copy .new { font-size: 27px; font-weight: 600; line-height: 1.05; white-space: nowrap; }

  .what-we-do { right: 66px; top: 893px; width: 380px; text-align: right; }
  .section-title { font-size: 36px; font-weight: 400; color: var(--mint); line-height: 1.2; white-space: nowrap; }
  .section-title b { color: var(--forest); font-weight: 700; }
  .what-we-do p { margin-top: 8px; font-size: 16px; line-height: 1.3; color: #333; white-space: nowrap; }

  .offer-panel {
    left: 0; top: 1152px; width: 1100px; height: 256px; background: var(--forest-deep);
    clip-path: polygon(634px 0, 1100px 0, 1100px 256px, 543px 256px);
  }
  .we-offer { right: 66px; top: 1168px; width: 440px; text-align: right; color: #fff; }
  .we-offer .section-title { color: #fff; }
  .we-offer .section-title b { color: var(--mint); }
  .we-offer p { margin-top: 4px; font-size: 23px; font-weight: 600; line-height: 1.2; white-space: nowrap; }

  /* footer */
  .contact {
    left: 66px; top: 1450px; width: 968px;
    display: flex; align-items: center; color: var(--ink); white-space: nowrap;
  }
  .contact > * { flex-shrink: 0; }
  .call { font-size: 29px; font-weight: 700; }
  .call span { font-weight: 400; }
  .phone-icon { width: 30px; height: 30px; margin: 0 10px 0 14px; }
  .phone { font-size: 42px; font-weight: 700; letter-spacing: .5px; }
  .divider { width: 2px; height: 46px; background: #888; margin: 0 28px; }
  .site { font-size: 38px; font-weight: 400; letter-spacing: 1.5px; }
  .site b { color: var(--mint); font-weight: 700; }
</style>
</head>
<body>
<main class="flyer">
  <svg class="abs hero-art" width="1100" height="500" viewBox="0 0 1100 500">
    <defs>
      <linearGradient id="sunsetSite" x1="0" y1="0" x2="0.4" y2="1">
        <stop offset="0" stop-color="#f2e3c4"/>
        <stop offset="0.35" stop-color="#e7b862"/>
        <stop offset="0.65" stop-color="#c98f3a"/>
        <stop offset="1" stop-color="#8a6440"/>
      </linearGradient>
    </defs>
    <polygon points="535,330 660,478 612,478" fill="#1b4328"/>
    <polygon points="480,0 1100,0 1100,477 650,477 560,300" fill="url(#sunsetSite)" role="img" aria-label="Photo of excavators working a construction site at sunset"/>
  </svg>

  <div class="abs brand">
    <span class="brand-mark"></span>
    <span class="brand-name">Ridgeway Builders<br>NY, Inc.</span>
  </div>
  <h1 class="abs headline">EXCAVATION</h1>
  <div class="abs subhead">CONCRETE STRUCTURAL</div>

  <section class="abs band-dark"></section>
  <p class="abs tagline">We'll Get The Job Done Rite The first Time!! NY'S<br>Leading Excavation, Foundation, Waterproofing<br>and Flat Roof Specialists</p>
  <h2 class="abs specialize">WE <b>SPECIALIZE</b> IN <span class="hot">CONCRETE CUTTING</span></h2>

  <ul class="abs service-col" style="left:66px">
    <li>Concrete Flatwork</li>
    <li>Concrete Repair</li>
    <li>Concrete Sidewalks</li>
    <li>Patios &amp; Driveways</li>
  </ul>
  <ul class="abs service-col" style="left:297px">
    <li>Patios</li>
    <li>Driveways</li>
    <li>Walkways</li>
    <li>Commercial Concrete<br>Work</li>
  </ul>
  <ul class="abs service-col" style="left:543px">
    <li>Concrete Restoration</li>
    <li>Building Alterations</li>
    <li>Foundations - Concrete</li>
    <li>Concrete Repairs</li>
  </ul>
  <ul class="abs service-col" style="left:806px">
    <li>Stoops, Porches And<br>Staircase</li>
    <li>Foundation Contractors<br>Concrete</li>
    <li>Facade Restoration</li>
    <li>Concrete</li>
  </ul>

  <section class="abs band-light"></section>
  <div class="abs machine-photo" role="img" aria-label="Photo of a yellow tracked excavator on a faded grey quarry background"></div>

  <div class="abs badge">
    <span class="burst"></span><span class="burst"></span><span class="burst"></span>
    <span class="burst"></span><span class="burst"></span><span class="burst"></span>
    <div class="badge-copy">
      <span class="deal"><span class="pct">10%</span><span class="off">OFF</span></span>
      <span class="for">FOR</span>
      <span class="new">NEW CUSTOMERS</span>
    </div>
  </div>

  <section class="abs what-we-do">
    <h3 class="section-title">WHAT <b>WE DO</b></h3>
    <p>Our projects include both Residential<br>and Commercial construction and<br>repairs/restorations. Occupied and fully<br>operational job sites are never a<br>problem. And we can also plan,<br>manage, and build multi-phase jobs.<br>we specialize in excavation, foundation,<br>Roofing and waterproofing.</p>
  </section>

  <section class="abs offer-panel"></section>
  <section class="abs we-offer">
    <h3 class="section-title">WE <b>OFFER</b></h3>
    <p>an end-to-end client experience<br>that includes seamless<br>communication, budgeting,<br>staffing, on-site organization, and<br>solid, quality handiwork every time</p>
  </section>

  <footer class="abs contact">
    <span class="call">Call <span>or</span> Text</span>
    <svg class="phone-icon" viewBox="0 0 32 32" aria-hidden="true">
      <rect width="32" height="32" rx="8" fill="#3fae5c"/>
      <path d="M11 8c1 0 2 3 2 4s-2 1.5-1.5 2.5 3 4 4 4.5 1.5-1.5 2.5-1.5 4 1 4 2-1.5 3.5-3.5 3.5C13 23 9 17 9 11c0-2 1-3 2-3z" fill="#fff"/>
    </svg>
    <span class="phone">555-014-2287</span>
    <span class="divider"></span>
    <span class="site">www.<b>rbwxpo</b>.com</span>
  </footer>
</main>
</body>
</html>
```